The project is a book cover for a health/recipe book for both Kindle and a future soft cover. Title is Morning Garden Table: Gather Greens and Steady Your Days with a subtitle Six Weeks of Gentle Kitchen Habits. I am a registed dietitian nutritionist specializing in midlife and senior women to help them look and feel 10 years younger by balancing hormones and curbing inflammationI like the idea of fresh colorful whole foods on the cover with a natural clean look. But I am also open to a cover which expresses vitality--perhaps a woman or couple whose "being" expresses energy and vitality.Since I am unsure right at this moment the exact # of pages for the book, I will need to have some wiggle room in the final stages to get the spine dimensions.I am happy to send a table of contents if that would help.I need to decide on a cover in the next 2 weeks. Below are some ideas on style that I like with reservations. Background on 1 is too dark, 2 is too pastel and 3 is good but doesn't move me as much and my followers liked it the least
Updates
Entered wrong completion date and would like more entries.
Target Market(s)
Woman 40 to 65+, college educated
Industry/Entity Type
Nutrition
Colors
Designer to choose colors to be used in the design.
Look and feel
Each slider illustrates characteristics of the customer's brand and the style your logo design should communicate.

```html
<!DOCTYPE html>
<html lang="en">
<head>
<meta charset="utf-8">
<title>Morning Garden Table – Book Cover</title>
<link rel="stylesheet" href="https://fonts.googleapis.com/css2?family=Montserrat:wght@300&family=Cabin:wght@600&family=Courgette&display=swap">
<style>
  :root {
    --page: #ffffff;
    --wood: #ebe4b6;
    --blush: #f3b9a4;
    --crimson: #de1f4e;
    --leaf-light: #b6dc7f;
    --leaf: #80c234;
    --title: #ffffff;
    --subtitle: #6a5d51;
    --ink: #1b1b1b;
    --ribbon: rgba(255,255,255,0.82);
  }
  html, body {
    margin: 0;
    width: 1200px;
    height: 998px;
    overflow: hidden;
    background: var(--page);
  }
  .cover {
    position: absolute;
    left: 187px;
    top: 0;
    width: 856px;
    height: 998px;
    overflow: hidden;
    background: var(--wood);
  }
  .cover-art {
    position: absolute;
    inset: 0;
  }
  .title {
    position: absolute;
    left: 0;
    width: 856px;
    margin: 0;
    font-family: "Montserrat", sans-serif;
    font-weight: 300;
    color: var(--title);
    text-shadow: 4px 6px 8px rgba(0,0,0,0.35);
    line-height: 1;
  }
  .title-main {
    top: 110px;
    text-align: center;
    font-size: 150px;
    letter-spacing: -2px;
  }
  .title-second {
    top: 270px;
    display: flex;
    justify-content: center;
    align-items: flex-start;
  }
  .title-small {
    font-size: 70px;
    margin-top: 12px;
    letter-spacing: -1px;
  }
  .title-large {
    font-size: 150px;
    letter-spacing: -2px;
  }
  .subtitle {
    position: absolute;
    top: 472px;
    left: 0;
    width: 856px;
    margin: 0;
    text-align: center;
    font-family: "Cabin", sans-serif;
    font-weight: 600;
    font-size: 44px;
    line-height: 74px;
    color: var(--subtitle);
  }
  .ribbon-text {
    position: absolute;
    left: 188px;
    width: 480px;
    text-align: center;
    font-family: "Courgette", cursive;
    color: var(--ink);
    margin: 0;
  }
  .ribbon-lead {
    top: 712px;
    font-size: 60px;
  }
  .ribbon-tail {
    top: 808px;
    font-size: 34px;
  }
</style>
</head>
<body>
<main class="cover">
  <svg class="cover-art" width="856" height="998" viewBox="0 0 856 998" xmlns="http://www.w3.org/2000/svg">
    <defs>
      <radialGradient id="salad-warm" cx="50%" cy="50%" r="50%">
        <stop offset="0%" stop-color="#c8584a"/>
        <stop offset="60%" stop-color="#5f8e3b"/>
        <stop offset="100%" stop-color="#e9e2dc"/>
      </radialGradient>
      <radialGradient id="roast-peppers" cx="50%" cy="50%" r="50%">
        <stop offset="0%" stop-color="#e8702a"/>
        <stop offset="65%" stop-color="#d9472d"/>
        <stop offset="100%" stop-color="#f4f1ee"/>
      </radialGradient>
      <radialGradient id="salad-green" cx="50%" cy="50%" r="50%">
        <stop offset="0%" stop-color="#5c8a3a"/>
        <stop offset="60%" stop-color="#7fae55"/>
        <stop offset="100%" stop-color="#f3f4f0"/>
      </radialGradient>
    </defs>

    <circle class="accent-blush" cx="135" cy="195" r="260" fill="var(--blush)"/>
    <circle class="accent-crimson" cx="720" cy="170" r="345" fill="var(--crimson)"/>
    <circle class="accent-leaf-light" cx="140" cy="800" r="270" fill="var(--leaf-light)"/>
    <circle class="accent-leaf" cx="660" cy="800" r="320" fill="var(--leaf)"/>

    <circle role="img" aria-label="Plate of green salad with grilled peaches" cx="105" cy="190" r="200" fill="url(#salad-warm)"/>
    <circle role="img" aria-label="Plate of roasted peppers, onion and mushrooms" cx="670" cy="120" r="240" fill="url(#roast-peppers)"/>
    <circle role="img" aria-label="Plate of mixed microgreen salad with flax seeds" cx="140" cy="820" r="190" fill="url(#salad-green)"/>
    <circle role="img" aria-label="Plate of leafy green salad with edible flowers" cx="680" cy="830" r="285" fill="url(#salad-green)"/>

    <path class="ribbon" d="M188 690 C 300 660, 400 700, 480 680 S 620 650, 668 665 L 668 890 C 600 910, 520 880, 440 905 S 280 920, 188 900 Z" fill="var(--ribbon)"/>
    <line class="ribbon-rule" x1="188" y1="790" x2="668" y2="790" stroke="var(--ink)" stroke-width="3"/>
  </svg>

  <h1 class="title title-main">MORNING</h1>
  <div class="title title-second">
    <span class="title-small">GARDEN</span><span class="title-large">TABLE</span>
  </div>

  <p class="subtitle">Gather Greens<br>and Steady Your Days</p>

  <p class="ribbon-text ribbon-lead">Six Weeks</p>
  <p class="ribbon-text ribbon-tail">of Gentle Kitchen Habits</p>
</main>
</body>
</html>
```